Harwick Legal

To update and modernize current business card appearance. Marta's business is based in Melbourne with 4 other lawyers in the firm. Marta travels to the Pilbara in Western Australia approximately 1 week a month as part of the firms legal work. She consults with clients in Newman, Tom Price and Port Hedland. The lawyers work mostly from a home office, apart from court appearances. They have a virtual office in Melbourne city, and use facilities in 3 or 4 other locations around Melbourne. It is important the client's think this is a conventional law firm with a permanent office. Our business structure is a difficult concept for them to grasp. The business has been operational for 3 years, growing from 1 lawyer to 4 lawyers during that time. Our website is www.Harwicklegal.example.au and is currently being upgraded as we are not happy with its content. The logo is currently orange and dark grey but the orange is a difficult colour to reproduce and often turns out "poo" brown when documents are printed. We need clients to know we are user friendly and caring - and not head up our rears ends as some lawyers appear to be.
Updates

Thank you for the feedback so far. 1. Some of the designs have too much black (We prefer darker grey & not too much.) 2. Happy for designers to play around with different colours & logo design. What we're after is a modern look and business card that people say "wow" when they pick it up.

Industry/Entity Type

Business

```html
<!DOCTYPE html>
<html lang="en">
<head>
<meta charset="utf-8">
<title>Harwick Legal – Business Card</title>
<link rel="stylesheet" href="https://fonts.googleapis.com/css2?family=Cinzel:wght@400;500&family=Open+Sans:wght@400;600;700&display=swap">
<style>
  :root {
    --backdrop: #8b5e3c;
    --card: #ffffff;
    --ink: #3a3a3a;
    --red: #d41f26;
    --red-deep: #8e1719;
    --silver-light: #f2f2f2;
    --silver-dark: #8c8c8c;
    --white: #ffffff;
  }
  * { margin: 0; padding: 0; box-sizing: border-box; }
  html, body { width: 1200px; height: 480px; overflow: hidden; }
  body {
    background: var(--backdrop);
    position: relative;
    font-family: "Open Sans", Arial, sans-serif;
  }
  .card {
    position: absolute;
    background: var(--card);
    box-shadow: 4px 5px 6px rgba(0,0,0,0.35);
    overflow: hidden;
  }
  .card--front { left: 79px; top: 89px; width: 481px; height: 271px; }
  .card--back  { left: 593px; top: 93px; width: 475px; height: 270px; }

  .front-panel { position: absolute; inset: 0; width: 100%; height: 100%; }

  .brand {
    position: absolute;
    display: flex;
    flex-direction: column;
    align-items: center;
    width: 240px;
  }
  .card--front .brand { left: -6px; top: 70px; }
  .card--back .brand  { left: 117px; top: 67px; }
  .brand__dot {
    width: 56px; height: 56px;
    border-radius: 50%;
    background: var(--red);
    margin-bottom: 22px;
  }
  .brand__name {
    font-family: "Cinzel", "Times New Roman", serif;
    font-weight: 500;
    font-size: 23px;
    color: var(--ink);
    letter-spacing: 0.5px;
    white-space: nowrap;
  }

  .holder-name {
    position: absolute;
    right: 27px; top: 29px;
    font-family: "Cinzel", "Times New Roman", serif;
    font-size: 17px;
    color: var(--white);
    letter-spacing: 0.5px;
  }
  .contact {
    position: absolute;
    right: 28px; top: 166px;
    text-align: right;
    color: var(--white);
    font-size: 11px;
    line-height: 19px;
    font-weight: 700;
  }
  .contact__address {
    margin-top: 3px;
    font-weight: 400;
    line-height: 15px;
  }
  .back-web {
    position: absolute;
    left: 0; right: 0; top: 208px;
    text-align: center;
    font-size: 11.5px;
    font-weight: 600;
    letter-spacing: 0.6px;
    color: var(--ink);
  }
</style>
</head>
<body>

  <section class="card card--front">
    <svg class="front-panel" viewBox="0 0 481 271" preserveAspectRatio="none" aria-hidden="true">
      <defs>
        <linearGradient id="silverBand" x1="0" y1="0" x2="1" y2="0">
          <stop offset="0" stop-color="var(--silver-dark)"/>
          <stop offset="0.55" stop-color="var(--silver-light)"/>
          <stop offset="1" stop-color="var(--silver-dark)"/>
        </linearGradient>
        <linearGradient id="redPanel" x1="0" y1="0" x2="1" y2="0">
          <stop offset="0" stop-color="var(--red)"/>
          <stop offset="0.6" stop-color="var(--red)"/>
          <stop offset="1" stop-color="var(--red-deep)"/>
        </linearGradient>
      </defs>
      <polygon points="271,0 481,0 481,271 271,271 221,136" fill="url(#silverBand)"/>
      <polygon points="293,0 481,0 481,271 293,271 243,136" fill="url(#redPanel)"/>
    </svg>

    <div class="brand">
      <span class="brand__dot"></span>
      <span class="brand__name">Harwick Legal</span>
    </div>

    <p class="holder-name">Your name here</p>

    <address class="contact" style="font-style:normal">
      <p>Tel: 012.345.6789</p>
      <p>Email: info@harwick.example</p>
      <p>www.Harwicklegal.example.au</p>
      <p class="contact__address">Suite 000, Cityname<br>country name</p>
    </address>
  </section>

  <section class="card card--back">
    <div class="brand">
      <span class="brand__dot"></span>
      <span class="brand__name">Harwick Legal</span>
    </div>
    <p class="back-web">www.Harwicklegal.example.au</p>
  </section>

</body>
</html>
```